Coffeeshop menu for filter tip

We want to have a cannabis (coffeeshop) menu in the size 25mm wide x 60mm wide. Some examples attached.

it must have the following text:
Menu

WEED p/g
Velotrine €16
Cinderfox €14
Tide Rambler €14
Marigolden €16
Grand Pelican €14
Copper Comet €14

HASH p/g
Baltic Ember €12
Harbor Velvet€11
Plum Rova €14
Dusk Maple €10

Target Market(s)

tourist in Amsterdam

Requirements
Nice to have
• cannabis sign leaf
• No Cigarettes allowed symbol

```html
<!DOCTYPE html>
<html lang="en">
<head>
<meta charset="utf-8">
<title>Amsterdam Menu</title>
<link href="https://fonts.googleapis.com/css2?family=Oswald:wght@600&family=Arimo:wght@700&family=Kaushan+Script&family=Playfair+Display:ital,wght@1,700&display=swap" rel="stylesheet">
<style>
  :root {
    --card-black: #0c0506;
    --card-wine: #3a0608;
    --pattern-red: #5a0a0c;
    --gold: #c9a23a;
    --yellow: #f7f000;
    --white: #ffffff;
    --marker-red: #e00000;
    --outline: #000000;
  }
  * { margin: 0; padding: 0; box-sizing: border-box; }
  html, body { width: 824px; height: 1200px; overflow: hidden; background: var(--card-black); }
  .menu-card {
    position: relative;
    width: 824px;
    height: 1200px;
    background: var(--card-black);
    overflow: hidden;
  }
  .pattern-field {
    position: absolute;
    left: 0; right: 0; top: 40px; bottom: 70px;
    background: radial-gradient(ellipse at 50% 55%, var(--pattern-red) 0%, var(--card-wine) 55%, var(--card-black) 100%);
  }
  .title-block { position: absolute; left: 0; right: 0; top: 40px; text-align: center; }
  .title-city {
    font-family: "Oswald", sans-serif;
    font-weight: 600;
    font-size: 72px;
    letter-spacing: 4px;
    color: var(--white);
    line-height: 1;
    text-shadow: 3px 3px 0 var(--outline);
  }
  .title-menu {
    font-family: "Arimo", sans-serif;
    font-weight: 700;
    font-size: 132px;
    color: var(--yellow);
    line-height: 1;
    margin-top: 2px;
    text-shadow: 4px 4px 0 var(--outline);
  }
  .section-heading {
    position: absolute;
    left: 80px;
    font-family: "Playfair Display", serif;
    font-style: italic;
    font-weight: 700;
    font-size: 72px;
    color: var(--white);
    -webkit-text-stroke: 2px var(--outline);
    text-shadow: 3px 3px 0 var(--outline);
    letter-spacing: 2px;
  }
  .unit-label {
    position: absolute;
    right: 110px;
    font-family: "Kaushan Script", cursive;
    font-size: 30px;
    color: var(--white);
    text-shadow: 2px 2px 0 var(--outline);
  }
  .price-list { position: absolute; left: 70px; right: 90px; list-style: none; }
  .price-item {
    display: flex;
    justify-content: space-between;
    align-items: baseline;
    height: 54px;
    font-family: "Kaushan Script", cursive;
    font-size: 36px;
    color: var(--yellow);
    text-shadow: 2px 2px 0 var(--outline);
  }
  .item-name { display: flex; align-items: center; }
  .item-name::before {
    content: "";
    display: inline-block;
    width: 0; height: 0;
    border-top: 10px solid transparent;
    border-bottom: 10px solid transparent;
    border-left: 16px solid var(--marker-red);
    margin-right: 22px;
  }
  .weed-heading { top: 250px; }
  .weed-unit { top: 345px; }
  .weed-list { top: 385px; }
  .hash-heading { top: 720px; }
  .hash-unit { top: 815px; }
  .hash-list { top: 855px; }
  .sign-row {
    position: absolute;
    left: 0; right: 0; bottom: 50px;
    display: flex;
    justify-content: center;
    gap: 60px;
  }
  .sign { width: 66px; height: 66px; }
</style>
</head>
<body>
<main class="menu-card">
  <div class="pattern-field" role="img" aria-label="Dark red baroque swirl pattern with gold flourishes"></div>

  <header class="title-block">
    <div class="title-city">AMSTERDAM</div>
    <h1 class="title-menu">MENU</h1>
  </header>

  <h2 class="section-heading weed-heading">WEED</h2>
  <div class="unit-label weed-unit">p/g</div>
  <ul class="price-list weed-list">
    <li class="price-item"><span class="item-name">Velotrine</span><span class="item-price">€ 16</span></li>
    <li class="price-item"><span class="item-name">Cinderfox</span><span class="item-price">€ 14</span></li>
    <li class="price-item"><span class="item-name">Tide Rambler</span><span class="item-price">€ 14</span></li>
    <li class="price-item"><span class="item-name">Marigolden</span><span class="item-price">€ 16</span></li>
    <li class="price-item"><span class="item-name">Grand Pelican</span><span class="item-price">€ 14</span></li>
    <li class="price-item"><span class="item-name">Copper Comet</span><span class="item-price">€ 14</span></li>
  </ul>

  <h2 class="section-heading hash-heading">HASH</h2>
  <div class="unit-label hash-unit">p/g</div>
  <ul class="price-list hash-list">
    <li class="price-item"><span class="item-name">Baltic Ember</span><span class="item-price">€ 12</span></li>
    <li class="price-item"><span class="item-name">Harbor Velvet</span><span class="item-price">€ 11</span></li>
    <li class="price-item"><span class="item-name">Plum Rova</span><span class="item-price">€ 14</span></li>
    <li class="price-item"><span class="item-name">Dusk Maple</span><span class="item-price">€ 10</span></li>
  </ul>

  <div class="sign-row">
    <svg class="sign cannabis-sign" viewBox="0 0 66 66" role="img" aria-label="Cannabis leaf sign">
      <circle cx="33" cy="33" r="32" fill="#ffffff"/>
      <circle cx="33" cy="33" r="18" fill="#1a1a1a"/>
    </svg>
    <svg class="sign no-smoking-sign" viewBox="0 0 66 66" role="img" aria-label="No cigarettes allowed">
      <circle cx="33" cy="33" r="32" fill="#ffffff"/>
      <rect x="14" y="32" width="34" height="7" fill="#1a1a1a"/>
      <rect x="48" y="32" width="5" height="7" fill="#1a1a1a"/>
      <path d="M44 28c0-5 4-5 4-10" stroke="#1a1a1a" stroke-width="2" fill="none"/>
      <circle cx="33" cy="33" r="25" fill="none" stroke="#e00000" stroke-width="6"/>
      <line x1="15" y1="15" x2="51" y2="51" stroke="#e00000" stroke-width="6"/>
    </svg>
  </div>
</main>
</body>
</html>
```